Thank You Card design for a federal credit union

I am looking to have a thank you card designed.
Specs:
Flat size of 9.5"x6.5" folds to final size of 4.75"x6.5", it will print full color on the front and back. Below, you will see their logo, which needs to print on the inside of the folded card. I also attached images of their current card. They would like to keep the blue color but are open to design on the front. This is a Federal Credit Union, so please make the design, modern and professional. Below is the text that needs to print below the logo on the inside of the card. The text and logo will print below the fold on the inside, leave the top portion (above the panel) white.
Inside text:
Our Members are the foundation of our Credit Union. We sincerely thank you for your loyalty, your business and the opportunity to serve you.
Target Market(s)
Clients of a federal credit union
Industry/Entity Type
Union
Requirements
Must have
- a simple, professional, and modern feel. "Thank You for your business" must be on the front section in some variation.
Should not have
- nothing flashy or too many colors. keep it simple

```html
<!DOCTYPE html>
<html lang="en">
<head>
<meta charset="utf-8">
<title>Thank You Card – Northfield Federal Credit Union</title>
<link href="https://fonts.googleapis.com/css2?family=Roboto:wght@400;500&family=Pinyon+Script&family=Almendra:wght@700&display=swap" rel="stylesheet">
<style>
  :root {
    --stage: #10116a;
    --card-deep: #0a0a22;
    --card-mid: #16164a;
    --leaf-blue: #2b3fc4;
    --leaf-light: #4a63e0;
    --badge: #1a237a;
    --ring: #6f86d8;
    --type-cyan: #5db8ec;
    --script-cyan: #7fd3f5;
    --paper: #ffffff;
    --fold: #e4e4ec;
    --ink: #1a1a2e;
  }
  * { margin: 0; padding: 0; box-sizing: border-box; }
  html, body { width: 1200px; height: 960px; overflow: hidden; }
  body { background: var(--stage); position: relative; font-family: "Roboto", Arial, sans-serif; }

  /* Front panel */
  .card-front {
    position: absolute; left: 110px; top: 330px; width: 450px; height: 300px;
    background: radial-gradient(circle at 45% 50%, var(--card-mid) 0%, var(--card-deep) 70%);
    overflow: hidden;
  }
  .leaf-wreath {
    position: absolute; left: 80px; top: 20px; width: 250px; height: 260px;
    border-radius: 50%;
    background: radial-gradient(circle, var(--leaf-light) 0%, var(--leaf-blue) 45%, rgba(43,63,196,0.35) 68%, rgba(43,63,196,0) 75%);
  }
  .greeting-badge {
    position: absolute; left: 120px; top: 65px; width: 170px; height: 170px;
    border-radius: 50%; background: var(--badge);
    display: flex; flex-direction: column; align-items: center; justify-content: center;
    text-align: center;
  }
  .greeting-badge::before {
    content: ""; position: absolute; inset: 6px; border-radius: 50%;
    border: 1.5px dashed var(--ring);
  }
  .greeting-lead, .greeting-tail { color: var(--type-cyan); text-transform: uppercase; line-height: 1.25; position: relative; }
  .greeting-lead { font-size: 10.5px; letter-spacing: 0.5px; }
  .greeting-lead strong { font-size: 12.5px; font-weight: 500; display: block; }
  .greeting-thanks {
    position: relative;
    font-family: "Pinyon Script", cursive; color: var(--script-cyan);
    font-size: 34px; line-height: 1.1; margin: 2px 0;
  }
  .greeting-tail { font-size: 11px; }
  .greeting-tail small { display: block; font-size: 8.5px; letter-spacing: 0.4px; }

  /* Inside spread */
  .card-inside {
    position: absolute; left: 640px; top: 180px; width: 450px; height: 600px;
    background: var(--paper);
  }
  .inside-top {
    height: 300px; background: var(--paper);
    border-bottom: 1px solid var(--fold);
  }
  .inside-bottom {
    height: 300px;
    padding: 24px 40px 0;
  }
  .union-name {
    display: flex; align-items: center; gap: 8px;
    font-weight: 500; font-size: 15px; color: var(--ink); margin-bottom: 16px;
  }
  .union-name .mark { width: 14px; height: 14px; background: var(--ink); }
  .inside-message {
    font-family: "Almendra", Georgia, serif; font-weight: 700;
    font-size: 12.5px; line-height: 1.45; color: var(--ink);
  }
</style>
</head>
<body>
  <section class="card-front">
    <div class="leaf-wreath" role="img" aria-label="Wreath of blue autumn maple and oak leaves"></div>
    <div class="greeting-badge">
      <p class="greeting-lead">We would<strong>like to say</strong></p>
      <p class="greeting-thanks">Thank You</p>
      <p class="greeting-tail">For your<small>Business</small></p>
    </div>
  </section>

  <section class="card-inside">
    <div class="inside-top"></div>
    <div class="inside-bottom">
      <div class="union-name"><span class="mark"></span>Northfield Federal Credit Union</div>
      <p class="inside-message">Our Members are the foundation of our Credit Union. We sincerely thank you for your loyalty, your business and the opportunity to serve you.</p>
    </div>
  </section>
</body>
</html>
```